Harlow Bidding Parallel Meter

I want a landing page for them to click on the logo with a brief description of the site.

Once they click on the logo, it will take them to make a decision for two types of insurance. One will be health and the other will be home/auto.

I will need an iframe for the home/auto and it will take them to a site (which is already built) for them to get a quote.

I will need a separate iframe for the health to take them to separate site (which is built) for them to get a quote.

Target Market(s)

18-45 Year olds who want to go online for insurance quotes. This is for quoting primarily and not an information site.

Industry/Entity Type

Health

Requirements
Must have
• Sleek and sexy. I have a logo as well.

May want the following on the landing page:
Georgia's FIRST Insurance Exchange for Home, Auto, and Health Insurance

No Hassle, Real-time, Quotes - As a Matter of fact... You call us if interested, We dont sell your information and Most Importantly… its free!!

Give it a shot… Click on the logo to get started and if you are interested in one of the many carriers we represent, call us.
Should not have
• Don't want the typical website. I want this to be different than all template boxes.

```html
<!DOCTYPE html>
<html lang="en">
<head>
<meta charset="utf-8">
<title>Harlow Bidding Parallel Meter – Insurance Quotes</title>
<link rel="stylesheet" href="https://fonts.googleapis.com/css2?family=Oswald:wght@400;500&family=Cabin:wght@400;600&family=Archivo+Black&display=swap">
<style>
  :root {
    --nav-red-top: #c8192a;
    --nav-red-bottom: #7e0d16;
    --nav-divider: #e0404c;
    --header-white: #ffffff;
    --sky: #b9e0f5;
    --navy-text: #1f3a5e;
    --heading-grey: #4b4b4b;
    --accent-red: #c8182a;
    --accent-blue: #2a86e0;
    --panel-border: #a6a6a6;
    --icon-dark: #2c3648;
    --footer-top: #14394d;
    --footer-bottom: #04121b;
    --footer-text: #ffffff;
  }
  * { box-sizing: border-box; margin: 0; padding: 0; }
  html, body { width: 1200px; height: 673px; overflow: hidden; }
  body { font-family: "Cabin", sans-serif; background: var(--sky); }

  .page { position: relative; width: 1200px; height: 673px; overflow: hidden; background: var(--sky); }

  .site-nav {
    position: absolute; left: 0; top: 0; width: 1200px; height: 78px;
    background: linear-gradient(var(--nav-red-top), var(--nav-red-bottom));
    display: flex; border-bottom: 2px solid #5c0810;
  }
  .site-nav a {
    font-family: "Oswald", sans-serif; font-weight: 500; font-size: 24px; color: #fff;
    text-decoration: none; text-transform: uppercase; line-height: 78px;
    white-space: nowrap;
  }
  .site-nav .nav-home { width: 156px; padding-left: 23px; border-right: 1px solid var(--nav-divider); }
  .site-nav .nav-quote { width: 222px; padding-left: 44px; border-right: 1px solid var(--nav-divider); }
  .site-nav .nav-contact { padding-left: 39px; }

  .site-header {
    position: absolute; left: 0; top: 80px; width: 1200px; height: 256px;
    background: linear-gradient(var(--header-white) 30%, #dff0fa 100%);
  }

  .brand {
    position: absolute; left: 30px; top: 160px;
    display: flex; align-items: center; gap: 14px;
  }
  .brand-dot { width: 44px; height: 44px; border-radius: 50%; background: var(--accent-red); }
  .brand-name { font-family: "Cabin", sans-serif; font-weight: 600; font-size: 31px; color: var(--icon-dark); }

  .intro { position: absolute; left: 392px; top: 97px; width: 785px; }
  .intro-title {
    font-family: "Archivo Black", sans-serif; font-size: 46px; line-height: 50px;
    color: var(--heading-grey); letter-spacing: 0.5px;
    text-shadow: 2px 2px 2px rgba(0,0,0,0.25);
  }
  .intro-lead, .intro-pitch { color: var(--navy-text); font-size: 21px; line-height: 26px; }
  .intro-lead { margin-top: 20px; }
  .intro-pitch { margin-top: 25px; }
  .intro-pitch .free { color: var(--accent-red); }

  .choice-panel {
    position: absolute; left: 201px; top: 318px; width: 803px; height: 275px;
    background: #fff; border: 2px solid var(--panel-border); border-radius: 48px;
    box-shadow: 0 3px 8px rgba(0,0,0,0.25);
  }
  .choice-heading {
    font-family: "Oswald", sans-serif; font-weight: 500; font-size: 39px;
    color: var(--accent-blue); text-align: center; line-height: 50px; margin-top: 16px;
    text-transform: uppercase;
  }
  .choice-list { position: absolute; left: 0; top: 73px; width: 100%; }
  .choice { position: absolute; width: 240px; text-align: center; text-decoration: none; }
  .choice--home { left: 23px; }
  .choice--auto { left: 283px; }
  .choice--life { left: 547px; }
  .choice-icon {
    display: block; width: 141px; height: 141px; margin: 0 auto; border-radius: 50%;
    background: #fff; padding: 8px; box-shadow: 0 2px 6px rgba(0,0,0,0.45);
  }
  .choice-icon span { display: block; width: 100%; height: 100%; border-radius: 50%; }
  .choice--home .choice-icon span { background: var(--accent-red); }
  .choice--auto .choice-icon span { background: var(--icon-dark); }
  .choice--life .choice-icon span { background: var(--icon-dark); }
  .choice-label {
    display: block; margin-top: 8px; font-family: "Oswald", sans-serif; font-size: 28px;
    color: var(--accent-red); text-transform: uppercase; line-height: 34px; white-space: nowrap;
  }

  .site-footer {
    position: absolute; left: 0; top: 610px; width: 1200px; height: 63px;
    background: linear-gradient(var(--footer-top), var(--footer-bottom));
    color: var(--footer-text); font-size: 18px; text-align: center; line-height: 60px;
  }
</style>
</head>
<body>
<div class="page">
  <nav class="site-nav">
    <a class="nav-home" href="#">Home Page</a>
    <a class="nav-quote" href="#">Quote Request</a>
    <a class="nav-contact" href="#">Contact Us</a>
  </nav>

  <header class="site-header">
    <div class="brand">
      <span class="brand-dot"></span>
      <span class="brand-name">Harlow Meter</span>
    </div>
  </header>

  <section class="intro">
    <h1 class="intro-title">INSURANCE</h1>
    <p class="intro-lead">Georgia's FIRST Insurance Exchange for Home, Auto, and Health Insu rance</p>
    <p class="intro-pitch">No Hassle, Real-time, Quotes - As a Matter of fact... You call us if interested, We dont sell your information and Most Importantly... <span class="free">ITS FREE!!</span></p>
  </section>

  <main class="choice-panel">
    <h2 class="choice-heading">Just click any logo to get started</h2>
    <div class="choice-list">
      <a class="choice choice--home" href="#">
        <span class="choice-icon"><span role="img" aria-label="Home insurance illustration of a house"></span></span>
        <span class="choice-label">Home Insurance</span>
      </a>
      <a class="choice choice--auto" href="#">
        <span class="choice-icon"><span role="img" aria-label="Auto insurance illustration of a car on a road"></span></span>
        <span class="choice-label">Auto Insurance</span>
      </a>
      <a class="choice choice--life" href="#">
        <span class="choice-icon"><span role="img" aria-label="Life insurance illustration of a person"></span></span>
        <span class="choice-label">Life Insurance</span>
      </a>
    </div>
  </main>

  <footer class="site-footer">© 2013, All Rights Reserved,&nbsp; Harlowmeter.com</footer>
</div>
</body>
</html>
```